Hero Image Redesign for VELM Consulting Website

About us:
VELM Consulting is an organisational psychology and human resource management consulting firm based in Melbourne, Australia (www.velmadvisory-example.com.au). We are a B2B offering a range of organisational psychology measurement and consulting. The largest part of our business is our online psychometric assessments, which are self-managed via an online portal, which is currently used by many organisations worldwide as part of their recruitment process.

What we are looking for:
We are seeking assistance to redesign an image located above the fold - on the top right hand side of homepage. We want an image of a small group of diverse people happily working together using a laptop (either individually or as a group), overlayed with graphic representations reflective of using our online Psychometric Assessment tool, in an interactive fashion.

The graphics will highlight key features of the self-service VELM Psychometric Assessment Portal, specifically ease of use, flexibility and our integrated approach. We want the image to look clean, clear, minimal, with use of negative space. All graphics must be accessible (including sufficient colour contrast and text size).

We would like the graphic to feature 3 “pop ups” highlighting features, and these should appear over the image:

1. Setup participants easily online
2. Check the status of an assessment
3. View participants’ reports

Examples from other SaaS websites attached.

The final design should communicate trust, reliability, our scientific evidence based approach, and our approachable and friendly customer service.

Our main brand colours are:
• Navy – HEX #2F2971
• Mid Blue – HEX #0C75C0
• Black – HEX #000000

About VELM’ website and potential for future work:

• VELM’ website pages have been created using Bricks Builder for WordPress.
• There is a strong possibility of future projects following successful delivery. We are an excellent client – ethical, professional and with a genuine commitment to partnership.

Need extra days to review

```html
<!DOCTYPE html>
<html lang="en">
<head>
<meta charset="utf-8">
<title>VELM Consulting – Organisational Psychology Consulting</title>
<link rel="stylesheet" href="https://fonts.googleapis.com/css2?family=Plus+Jakarta+Sans:wght@400;500;700;800&family=Roboto:wght@400;500&display=swap">
<style>
  :root {
    --navy: #2F2971;
    --teal: #8ee0d8;
    --teal-soft: #a8e6df;
    --teal-pale: #cdf1ed;
    --teal-ring: #cbf0ec;
    --nav-bg: #f5f5f5;
    --ink: #2a2a2a;
    --body: #454545;
    --white: #ffffff;
  }
  * { margin: 0; padding: 0; box-sizing: border-box; }
  html, body { width: 1200px; height: 623px; overflow: hidden; background: var(--white); }
  body { position: relative; font-family: "Plus Jakarta Sans", sans-serif; color: var(--ink); }

  .announce-bar {
    position: absolute; left: 0; top: 0; width: 1200px; height: 35px;
    background: var(--navy); color: var(--white);
    display: flex; align-items: center; justify-content: center;
    font-size: 11.5px; font-weight: 500; letter-spacing: -0.1px;
  }
  .announce-bar a { color: var(--teal); text-decoration: underline; }
  .announce-bar .divider { margin: 0 5px; }

  .site-nav {
    position: absolute; left: 0; top: 35px; width: 1200px; height: 57px;
    background: var(--nav-bg);
  }
  .brand {
    position: absolute; left: 100px; top: 16px;
    display: flex; align-items: center; gap: 7px;
    font-size: 22px; font-weight: 800; color: var(--navy); letter-spacing: -0.3px;
  }
  .brand-mark { width: 18px; height: 18px; background: var(--teal-soft); border-radius: 3px; }
  .nav-menu {
    position: absolute; left: 378px; top: 0; height: 57px;
    display: flex; align-items: center; list-style: none;
    font-size: 11.5px; font-weight: 500; color: var(--ink);
  }
  .nav-menu li { display: flex; align-items: center; gap: 6px; margin-right: 24px; }
  .nav-menu li:last-child { margin-right: 0; }
  .nav-menu svg { width: 9px; height: 6px; }

  .hero-copy { position: absolute; left: 131px; top: 148px; width: 480px; }
  .hero-title {
    font-size: 53px; font-weight: 700; line-height: 60px; color: var(--navy);
    letter-spacing: -0.3px;
  }
  .hero-title .accent { color: var(--teal); }
  .hero-lead {
    margin-top: 26px; font-size: 19.5px; line-height: 34px; color: var(--body);
    font-weight: 400; letter-spacing: -0.2px; width: 470px;
  }
  .hero-actions { position: absolute; left: 131px; top: 468px; display: flex; gap: 32px; }
  .btn {
    height: 46px; display: flex; align-items: center; justify-content: center;
    font-size: 13.5px; font-weight: 700; border-radius: 2px;
    box-shadow: 0 2px 4px rgba(0,0,0,0.15);
  }
  .btn-primary { width: 175px; background: var(--navy); color: var(--white); }
  .btn-secondary { width: 174px; background: var(--teal-soft); color: var(--navy); gap: 8px; }

  .portal-graphic { position: absolute; left: 660px; top: 150px; width: 520px; height: 440px; }
  .portal-graphic > svg { position: absolute; left: 0; top: 0; }
  .team-photo {
    position: absolute; left: 95px; top: 100px; width: 248px; height: 248px; border-radius: 50%;
    background: radial-gradient(circle at 45% 40%, #d9d6d0 0%, #9a948c 55%, #5e5954 100%);
  }
  .feature-pop {
    position: absolute; width: 150px; height: 71px; border-radius: 8px;
    display: flex; align-items: center; gap: 10px; padding: 0 10px 0 12px;
    font-family: "Roboto", sans-serif; font-size: 11.5px; line-height: 15px;
  }
  .feature-pop .icon {
    flex: 0 0 26px; width: 26px; height: 26px; border-radius: 50%;
    display: flex; align-items: center; justify-content: center;
  }
  .pop-setup { left: 32px; top: 49px; background: var(--teal-pale); color: #111; }
  .pop-setup .icon { background: var(--navy); }
  .pop-status { left: 286px; top: 21px; background: var(--white); border: 2px solid var(--navy); color: #111; }
  .pop-status .icon { background: var(--navy); }
  .pop-reports { left: 337px; top: 238px; background: var(--navy); color: var(--white); }
  .pop-reports .icon { background: var(--teal-soft); }
</style>
</head>
<body>
  <div class="announce-bar">
    Register now for our&nbsp;<a href="#">free virtual workshops</a>
    <span class="divider">|</span>
    VELM Consulting Clients:&nbsp;<a href="#">Login to the Portal</a>
  </div>

  <nav class="site-nav">
    <div class="brand"><span class="brand-mark"></span>VELM Consulting</div>
    <ul class="nav-menu">
      <li>Psychometric testing <svg viewBox="0 0 9 6"><path d="M1 1l3.5 3.5L8 1" fill="none" stroke="#2a2a2a" stroke-width="1.5"/></svg></li>
      <li>Employee wellbeing <svg viewBox="0 0 9 6"><path d="M1 1l3.5 3.5L8 1" fill="none" stroke="#2a2a2a" stroke-width="1.5"/></svg></li>
      <li>HR consulting <svg viewBox="0 0 9 6"><path d="M1 1l3.5 3.5L8 1" fill="none" stroke="#2a2a2a" stroke-width="1.5"/></svg></li>
      <li>Events</li>
      <li>Knowledge hub <svg viewBox="0 0 9 6"><path d="M1 1l3.5 3.5L8 1" fill="none" stroke="#2a2a2a" stroke-width="1.5"/></svg></li>
      <li>About us <svg viewBox="0 0 9 6"><path d="M1 1l3.5 3.5L8 1" fill="none" stroke="#2a2a2a" stroke-width="1.5"/></svg></li>
      <li>Contact</li>
    </ul>
  </nav>

  <section class="hero-copy">
    <h1 class="hero-title">Organisational<br><span class="accent">Psychology</span><br>Consulting</h1>
    <p class="hero-lead">Optimise your workforce with psychometric testing, engagement surveys, wellbeing measures, and organisational development.</p>
  </section>
  <div class="hero-actions">
    <a class="btn btn-primary">Psychometric Testing</a>
    <a class="btn btn-secondary">Speak to an Expert
      <svg width="10" height="9" viewBox="0 0 10 9"><path d="M0 4.5h8.5M5 1l3.5 3.5L5 8" fill="none" stroke="#2F2971" stroke-width="1.2"/></svg>
    </a>
  </div>

  <div class="portal-graphic">
    <svg width="520" height="440" viewBox="0 0 520 440">
      <circle cx="219" cy="224" r="200" fill="none" stroke="var(--teal-ring)" stroke-width="3.5"/>
      <circle cx="219" cy="224" r="165" fill="none" stroke="var(--navy)" stroke-width="4.5"/>
      <circle cx="219" cy="224" r="143" fill="none" stroke="#eefaf8" stroke-width="6"/>
      <circle cx="219" cy="224" r="127" fill="none" stroke="var(--teal-ring)" stroke-width="3"/>
      <path d="M52 118 L40 140 L65 118 Z" fill="var(--teal-pale)"/>
      <path d="M292 88 L290 118 L310 90 Z" fill="var(--white)" stroke="var(--navy)" stroke-width="2" stroke-linejoin="round"/>
      <path d="M347 306 L345 340 L368 306 Z" fill="var(--navy)"/>
    </svg>
    <div class="team-photo" role="img" aria-label="Photo of a diverse team smiling while working together around a laptop"></div>

    <div class="feature-pop pop-setup">
      <span class="icon"><svg width="12" height="12" viewBox="0 0 12 12"><circle cx="6" cy="6" r="3.6" fill="none" stroke="#fff" stroke-width="2.4" stroke-dasharray="1.6 1.2"/><circle cx="6" cy="6" r="2.3" fill="#fff"/><circle cx="6" cy="6" r="1" fill="#2F2971"/></svg></span>
      <span>Setup participants easily online</span>
    </div>
    <div class="feature-pop pop-status">
      <span class="icon"><svg width="12" height="11" viewBox="0 0 12 11"><rect x="0.8" y="0.8" width="10.4" height="7" rx="1" fill="none" stroke="#fff" stroke-width="1.5"/><path d="M4 10h4M6 8v2" stroke="#fff" stroke-width="1.4"/></svg></span>
      <span>Check the status of an assessment</span>
    </div>
    <div class="feature-pop pop-reports">
      <span class="icon"><svg width="12" height="8" viewBox="0 0 12 8"><path d="M0.5 4C2 1.5 4 0.5 6 0.5S10 1.5 11.5 4C10 6.5 8 7.5 6 7.5S2 6.5 0.5 4Z" fill="none" stroke="#2F2971" stroke-width="1.2"/><circle cx="6" cy="4" r="1.8" fill="#2F2971"/></svg></span>
      <span>View participants’ reports</span>
    </div>
  </div>
</body>
</html>
```